Purchasing community for life science startups needs landing page for collecting of contact adresses

We are the "Pipette Union", the first purchasing community for life science startups. The idea is to bundle the needs of several smaller companies (laboratories) and to buy lab consumables and chemicals in larger quantities. This bargaining position, at the end of all participants can buy their products very low prices. In the attached powerpoint file you will find an idea and some elements, which demonstrate a little the style, which came into my mind.
Urlaub/Ferien
Target Market(s)
Our target customers are startups and smaller biotech companies, which are too small to get the best prices. The aim of this landing page is to collect all interested parties.
Look and feel

```html
<!DOCTYPE html>
<html lang="de">
<head>
<meta charset="utf-8">
<title>Pipette Union – Gemeinsam einkaufen</title>
<link href="https://fonts.googleapis.com/css2?family=Open+Sans:ital,wght@0,400;0,600;0,700;1,600&display=swap" rel="stylesheet">
<style>
:root{
  --navy:#0d3b6e;
  --cyan:#1aa7e3;
  --text:#555b63;
  --grey-bg:#ecebe8;
  --white:#ffffff;
  --footer:#3c6cc4;
  --hero-a:#3e6aa8;
  --field:#39b4e8;
}
*{box-sizing:border-box;margin:0;padding:0}
html,body{width:1200px;height:2791px;overflow:hidden}
body{font-family:"Open Sans",Arial,sans-serif;color:var(--text);background:var(--white);position:relative}
.abs{position:absolute}
.site-header{position:absolute;top:0;left:0;width:1200px;height:102px;background:var(--white)}
.brand{left:200px;top:22px;display:flex;align-items:center;gap:12px}
.brand-mark{width:58px;height:58px;background:var(--navy)}
.brand-name{font-weight:700;font-size:24px;color:var(--navy);line-height:1.05}
.brand-name small{display:block;font-size:13px;font-weight:600}
.nav{left:600px;top:44px;display:flex;gap:42px;font-weight:700;font-size:14px;color:var(--navy)}
.hero{position:absolute;left:0;width:1200px;text-align:center;color:var(--white)}
.hero-photo{position:absolute;inset:0}
.hero h1{position:absolute;left:0;right:0;font-weight:700;font-size:35px;line-height:40px;text-transform:uppercase}
.hero .intro{position:absolute;left:0;right:0;font-size:14.5px;line-height:26px}
.hero .callout{position:absolute;left:50%;transform:translateX(-50%);white-space:nowrap;font-weight:700;font-size:22px;line-height:28px;padding:8px 18px;color:var(--white)}
.btn-ghost{left:515px;width:168px;height:46px;border:2px solid var(--white);font-weight:700;font-size:17px;line-height:42px;color:var(--white)}
.mouse{left:589px}
.band-grey{position:absolute;left:0;top:532px;width:1200px;height:408px;background:var(--grey-bg)}
.section-title{position:absolute;left:0;right:0;text-align:center;font-weight:700;font-size:36px;color:var(--navy)}
.section-title .pct{color:#c9c9c9}
.product-photo{position:absolute}
.checklist{list-style:none;font-weight:600;font-size:15.5px;line-height:21px;color:#6b6f74}
.checklist li{display:flex;align-items:center;gap:12px}
.checklist li::before{content:"";width:10px;height:10px;border:2px solid var(--cyan)}
.invite{font-size:14.5px;line-height:21px;color:#7a7e83}
.invite a{color:var(--cyan);font-style:italic;font-weight:600}
.signup-card{position:absolute;width:402px;height:476px;background:var(--white);border:1px solid #d4d4d4;box-shadow:0 2px 6px rgba(0,0,0,.12);padding:30px 44px 0 42px}
.signup-card .lead{font-size:13.5px;line-height:20px;color:#7a7e83}
.signup-card .questions{margin-top:14px;font-weight:600;font-size:13.5px;line-height:20px;color:var(--cyan)}
.field{margin-top:20px}
.field label{display:block;font-weight:700;font-size:11px;color:var(--navy);margin-bottom:5px}
.field span{display:block;height:30px;border:1px solid var(--field)}
.btn-primary{display:block;margin-top:32px;height:56px;background:var(--cyan);color:var(--white);font-weight:700;font-size:13px;text-align:center;line-height:56px;border-radius:3px}
.copy{position:absolute;width:410px;font-size:14px;line-height:21px;color:#5d6167}
.copy p{margin-bottom:21px}
.copy strong{color:var(--navy);font-weight:700}
.site-footer{position:absolute;left:0;top:2576px;width:1200px;height:215px;background:var(--footer);color:var(--white);padding:76px 0 0 172px;font-size:19px;line-height:30px}
</style>
</head>
<body>

<header class="site-header">
  <div class="abs brand">
    <span class="brand-mark"></span>
    <span class="brand-name">PIPETTE UNION<small>Einkaufsverbund LifeScience</small></span>
  </div>
  <nav class="abs nav"><span>VORTEILE</span><span>JOINT PURCHASE</span></nav>
</header>

<section class="hero" style="top:102px;height:430px">
  <div class="hero-photo" role="img" aria-label="Laborglas mit blauen, grünen und gelben Flüssigkeiten" style="background:linear-gradient(100deg,#6f8fb9 0%,var(--hero-a) 45%,#4d79b0 70%,#7e9a6a 100%)"></div>
  <h1 style="top:38px">Gemeinsam einkaufen zu<br>Großhandelspreisen</h1>
  <p class="intro" style="top:128px">Betreibst du ein LifeScience Labor?<br>Benötigst du regelmäßig Chemikalien, Laborglas und Verbrauchsmaterialien?<br>Sind deine Abnahmemengen zu klein, um maximale Rabatte zu erhalten?</p>
  <p class="callout" style="top:226px;background:var(--cyan)">Dann mach mit bei der ersten Pipette Union 2019 und<br>spare bis zu 40% im Einkauf.</p>
  <span class="abs btn-ghost" style="top:320px">Lesen Sie mehr</span>
  <svg class="abs mouse" style="top:388px" width="20" height="34" viewBox="0 0 20 34"><rect x="2" y="2" width="16" height="30" rx="8" fill="none" stroke="#1aa7e3" stroke-width="2.5"/><line x1="10" y1="8" x2="10" y2="14" stroke="#1aa7e3" stroke-width="2.5"/></svg>
</section>

<div class="band-grey"></div>
<h2 class="section-title" style="top:560px">VORTEILE <span class="pct">%</span></h2>
<div class="product-photo" role="img" aria-label="Versandkarton aus Pappe" style="left:170px;top:615px;width:240px;height:265px;background:linear-gradient(150deg,#d2ae7f,#a8825a)"></div>
<ul class="abs checklist" style="left:625px;top:642px">
  <li>Kaufe ein zu Großhandelspreisen</li>
  <li>Keine Verhandlungen mit Lieferanten</li>
  <li>Keine Vertragsverpflichtung</li>
</ul>
<p class="abs invite" style="left:625px;top:722px;width:360px">Hast du Interesse an einer Teilnahme?<br>Dann trage dich gerne völlig unverbindlich in <a>unsere Interessentenliste ein.</a></p>

<div class="signup-card" style="left:626px;top:820px">
  <p class="lead">Um einen Eindruck von unseren Preisen zu erhalten schicken wir dir eine vorläufige Preisliste zu und bitten dich um feedback.</p>
  <p class="questions">Welche Artikel interessieren dich?<br>In welchen Mengen benötigst du diese?<br>Welche fehlen noch?</p>
  <div class="field"><label>Email Address:</label><span></span></div>
  <div class="field"><label>Last Name:</label><span></span></div>
  <div class="field"><label>First Name:</label><span></span></div>
  <span class="btn-primary">PREISLISTE PER EMAIL ERHALTEN</span>
</div>

<div class="copy" style="left:172px;top:992px">
  <p><strong>Unser Ziel</strong> ist der Aufbau der ersten Einkaufsgemeinschaft für LifeScience Labore, über die jeder Teilnehmer seinen Laborbedarf zu Großhandelspreisen decken kann.</p>
  <p><strong>Das Kampagnenprinzip.</strong> Wir bündeln euren Jahresbedarf an Chemikalien, Verbrauchsmaterialien und Laborbedarf und treten den Herstellern und Lieferanten gegenüber als ein starker Verhandlungspartner auf. Je mehr Teilnehmer mitmachen, desto größer wird unsere Verhandlungsmasse, desto besser unsere Einkaufspreise.</p>
  <p><strong>Keep it simple.</strong> Wir verzichten auf Rahmenverträge, Mindestbestellmengen und sonstigen Verpflichtungen! Gefällt euch der ausgehandelte Preis, dann bezieht ihr ganz normal per Bestellung bei der Pipette Union euren Bedarf.</p>
</div>

<section class="hero" style="top:1370px;height:427px">
  <div class="hero-photo" role="img" aria-label="Wissenschaftlerin mit Schutzbrille bei der Arbeit im Labor" style="background:linear-gradient(95deg,#3d5578 0%,#6d86a8 40%,#9fb2c9 70%,#c9d3de 100%)"></div>
  <h1 style="top:28px">Joint purchase at wholesale prices</h1>
  <p class="intro" style="top:118px">Do you run a LifeScience lab?<br>Do you need chemicals, laboratory glassware and consumables regularly?<br>Are your purchase quantities too small to receive maximum discounts?</p>
  <p class="callout" style="top:212px;background:var(--navy)">Then take part in the first lab campaign 2019 and<br>Save up to 40% on purchases.</p>
</section>

<h2 class="section-title" style="top:1822px">BENEFITS FOR PARTICIPANTS</h2>
<div class="product-photo" role="img" aria-label="Drei gestapelte Versandkartons" style="left:200px;top:1895px;width:290px;height:290px;background:linear-gradient(150deg,#d2ae7f,#a8825a)"></div>
<ul class="abs checklist" style="left:625px;top:1904px">
  <li>Buy at wholesale prices</li>
  <li>No negotiations with suppliers</li>
  <li>No contract obligation</li>
</ul>
<p class="abs invite" style="left:625px;top:1986px;width:330px">Are you interested in participating?<br>Then please do not hesitate to sign up for our list of interested parties.</p>

<div class="signup-card" style="left:626px;top:2080px">
  <p class="lead">To get an impression of our prices, we send you a preliminary price list and ask for feedback. Which articles interest you? In what quantities do you need these? Which are still missing?</p>
  <div class="field" style="margin-top:26px"><label>Email Address:</label><span></span></div>
  <div class="field"><label>Last Name:</label><span></span></div>
  <div class="field"><label>First Name:</label><span></span></div>
  <span class="btn-primary">PREISLISTE PER EMAIL ERHALTEN</span>
</div>

<div class="copy" style="left:172px;top:2214px">
  <p><strong>Our goal</strong> is to build the first LifeScience Laboratory purchasing community, which allows each participant to cover their laboratory supplies at wholesale prices.</p>
  <p><strong>The campaign principle.</strong> We bundle your annual demand for chemicals, consumables and laboratory supplies and act as a strong negotiating partner for manufacturers and suppliers. The more participants participate, the bigger our bargaining power, the better our purchase prices.</p>
  <p><strong>Keep it simple.</strong> We waive framework contracts, minimum order quantities and other obligations! If you like the negotiated price, then you normally order by order in the laboratory campaign your needs.</p>
</div>

<footer class="site-footer">
  Pipette Union Einkaufsverbund e.K.<br>IMPRESSUM | DATENSCHUTZERKLÄRUNG
</footer>

</body>
</html>
```